Postcard double sided

Title: DWIGHT'S REVENGE

Why would Dwight Kessler align himself with Gordon Pruett?

(photo of two guys)

Dwight approached elected officials that he wanted to run for office, but did not have money to finance his campaign. He wanted other elected officials to finance his campaign. Everyone told him that they would help him get the vote out, but that he needed to finance his own race.

In comes Gordon Pruett.

Gordon Pruett who has a pay to play scheme over at the City, told Dwight he would finance his campaign on one condition.

He needed to run against Steven Hulse.

Why would Dwight want to run with no money?

Backside

DWIGHT'S REVENGE

Dwight decided to run because no one on the school board would terminate Dwight's ex and her new boyfriend who both work for the school district. His ex even filed criminal charges against him that are still pending.

Mug Shot facing left (name the charges Criminal Trespass , and Criminal Mischief (highlight bold letters use two lines) mug shot facing right

Complaint one (then photo with full face) Compliant 2)
(showcharges)

Dwight's ultimate goal is to terminate his ex and her new boyfriend if elected.
Plus Gordon Pruett needs the majority on the school board to do what he does bet.

Kickbacks for Contracts.

They will hire their own contractors!
Say "No" to Dwight's Revenge and Gordon Pruett Money Grab!

Title On Back: all caps: DOMESTIC VIOLENCE

```html
<!DOCTYPE html>
<html lang="en">
<head>
<meta charset="utf-8">
<title>Dwight's Revenge – Postcard</title>
<link rel="stylesheet" href="https://fonts.googleapis.com/css2?family=Montserrat:ital,wght@0,700;0,800;0,900;1,800;1,900&family=Lato:wght@400;700;900&display=swap">
<style>
  :root{
    --stage:#8e939c;
    --red:#c0242b;
    --red-dark:#9e1c22;
    --navy:#262d45;
    --navy-deep:#1c2440;
    --blue:#3f5da0;
    --blue-soft:#5c77b5;
    --lavender:#c9cfe6;
    --orange:#e7a21f;
    --ink:#1f2430;
    --white:#ffffff;
  }
  *{box-sizing:border-box;margin:0;padding:0}
  html,body{width:1200px;height:1200px;overflow:hidden}
  body{background:var(--stage);font-family:"Lato",Arial,sans-serif;color:var(--ink);position:relative}
  .card{position:absolute;left:160px;background:var(--white);overflow:hidden;box-shadow:0 10px 24px rgba(0,0,0,.35)}
  .abs{position:absolute}
  .shapes{position:absolute;left:0;top:0}

  /* ---------- front ---------- */
  .front{top:104px;width:908px;height:494px}
  .front .header{left:0;top:0;width:908px;height:74px;background:var(--red)}
  .front .header-rule{left:0;top:77px;width:908px;height:2px;background:var(--red)}
  .title{font-family:"Montserrat",Arial,sans-serif;font-weight:800;color:var(--white);font-size:45px;letter-spacing:1px;left:18px;top:10px;white-space:nowrap}
  .subtitle{left:500px;top:16px;width:390px;text-align:center;color:var(--white);font-weight:700;font-size:17px;line-height:21px;letter-spacing:.3px}
  .intro{left:120px;top:83px;width:776px;text-align:right;font-size:16px;line-height:19px;color:var(--ink)}
  .in-comes{left:510px;top:166px;font-size:24px;font-weight:700;color:var(--navy);white-space:nowrap}
  .in-comes .name{color:var(--red)}
  .in-comes-rule{left:510px;top:197px;width:300px;height:3px;background:var(--orange)}
  .offer{left:460px;top:289px;width:429px;text-align:right;color:var(--white);font-size:16px;line-height:20px}
  .offer u{text-decoration:none;border-bottom:3px solid var(--white);padding-bottom:2px}
  .condition{left:300px;top:398px;width:581px;text-align:right;font-weight:900;font-size:18px;color:var(--navy)}
  .condition .name{color:var(--red)}
  .front .footer{left:0;top:446px;width:908px;height:48px;background:var(--navy);display:flex;align-items:center;justify-content:center}
  .front .footer p{font-family:"Montserrat",Arial,sans-serif;font-weight:900;font-style:italic;font-size:21px;color:var(--white);letter-spacing:.4px}

  /* ---------- back ---------- */
  .back{top:652px;width:910px;height:496px}
  .back .title-back{left:18px;top:12px;font-family:"Montserrat",Arial,sans-serif;font-weight:900;font-style:italic;font-size:29px;color:var(--white);letter-spacing:.5px;white-space:nowrap}
  .lede{left:20px;top:57px;width:790px;color:var(--white);font-size:14.5px;line-height:19px}
  .stamp,.address{background:var(--white);display:flex;align-items:center;justify-content:center;font-size:13px;color:var(--ink)}
  .stamp{left:812px;top:20px;width:75px;height:77px}
  .address{left:717px;top:113px;width:170px;height:67px}
  .mug{background:var(--white);padding:5px;box-shadow:0 3px 8px rgba(0,0,0,.35)}
  .mug span{display:block;width:100%;height:100%;background:linear-gradient(180deg,#b5b8bc 0%,#9a9ea4 60%,#2f4a36 100%)}
  .mug-left{left:30px;top:104px;width:86px;height:94px}
  .mug-center{left:221px;top:170px;width:96px;height:118px}
  .mug-right{left:430px;top:104px;width:94px;height:94px}
  .charges{left:141px;top:104px;width:276px;height:58px;border:3px solid var(--red);outline:1px solid var(--red);outline-offset:-7px;background:var(--white);text-align:center;color:var(--red);font-weight:900;font-size:18.5px;line-height:20px;padding-top:7px;box-shadow:0 2px 6px rgba(0,0,0,.2)}
  .complaint{top:292px;height:140px;font-family:"Lato",Arial,sans-serif;font-size:5px;line-height:6.4px;color:#222}
  .complaint-one{left:28px;width:282px}
  .complaint-two{left:320px;width:316px}
  .complaint .head{display:flex;justify-content:space-between;font-weight:700;margin-bottom:6px}
  .complaint p{margin-bottom:4px}
  .complaint .sign{display:flex;justify-content:space-between;margin-top:10px}
  .complaint .sign-line{display:inline-block;width:80px;border-bottom:1px solid #222;margin-left:4px}
  .goal{left:717px;top:200px;width:175px;color:var(--white);font-weight:700;font-size:12.5px;line-height:15.5px}
  .kickbacks{left:645px;top:304px;width:265px;height:64px;background:var(--red);color:var(--white);font-family:"Montserrat",Arial,sans-serif;font-weight:900;font-style:italic;font-size:24px;line-height:27px;padding:6px 0 0 48px}
  .contractors{left:645px;top:368px;width:265px;height:70px;background:var(--blue);color:var(--white);text-align:center;font-weight:700;font-size:16.5px;line-height:21px;padding-top:8px}
  .back .footer{left:0;top:438px;width:910px;height:58px;background:var(--red);display:flex;align-items:center;justify-content:center;gap:10px;color:var(--white);font-family:"Montserrat",Arial,sans-serif;font-style:italic;font-weight:900}
  .back .footer .say{font-size:34px}
  .back .footer .rest{font-size:21px;font-weight:800}
</style>
</head>
<body>

<!-- Front of postcard -->
<section class="card front">
  <svg class="shapes" width="908" height="494" viewBox="0 0 908 494">
    <defs>
      <linearGradient id="photoTone" x1="0" y1="0" x2="1" y2="1">
        <stop offset="0" stop-color="#2c3f74"/>
        <stop offset=".55" stop-color="#3a4a6e"/>
        <stop offset="1" stop-color="#23283a"/>
      </linearGradient>
      <linearGradient id="stripTone" x1="0" y1="0" x2="1" y2="0">
        <stop offset="0" stop-color="#c4cbe3"/>
        <stop offset="1" stop-color="#ffffff"/>
      </linearGradient>
    </defs>
    <polygon points="470,250 908,190 908,446 430,446" fill="var(--blue)"/>
    <polygon points="620,240 908,205 908,240 640,260" fill="var(--blue-soft)" opacity=".5"/>
    <rect x="300" y="392" width="608" height="34" fill="url(#stripTone)"/>
    <polygon points="0,101 520,241 450,446 0,446" fill="url(#photoTone)" role="img" aria-label="Photo of Dwight Kessler and Gordon Pruett smiling side by side in front of a campaign backdrop"/>
    <line x1="0" y1="99" x2="520" y2="239" stroke="var(--orange)" stroke-width="5"/>
  </svg>

  <div class="abs header"></div>
  <div class="abs header-rule"></div>
  <h1 class="abs title">DWIGHT'S REVENGE</h1>
  <p class="abs subtitle">WHY WOULD DWIGHT KESSLER<br>ALIGN HIMSELF WITH GORDON PRUETT?</p>

  <p class="abs intro">Dwight approached elected officials that he wanted to run for office, but did not have money to finance his campaign. He wanted other elected officials to finance his campaign. Everyone told him that they would help him get the vote out, but that he needed to finance his own race.</p>

  <p class="abs in-comes">IN COMES <span class="name">Gordon Pruett.</span></p>
  <div class="abs in-comes-rule"></div>

  <p class="abs offer">Gordon Pruett<br>who has a pay to play scheme<br>over at the City, told Dwight he would<br>finance his campaign on <u>ONE CONDITION:</u></p>

  <p class="abs condition">HE NEEDED TO RUN AGAINST <span class="name">STEVEN HULSE</span></p>

  <div class="abs footer"><p>WHY WOULD DWIGHT WANT TO RUN WITH NO MONEY?</p></div>
</section>

<!-- Back of postcard -->
<section class="card back">
  <svg class="shapes" width="910" height="496" viewBox="0 0 910 496">
    <polygon points="0,96 680,96 680,300 0,300" fill="#eef0f8"/>
    <polygon points="0,96 300,96 0,250" fill="var(--lavender)" opacity=".7"/>
    <polygon points="300,96 640,96 470,240" fill="var(--lavender)" opacity=".55"/>
    <rect x="0" y="0" width="740" height="53" fill="var(--red)"/>
    <rect x="0" y="53" width="820" height="43" fill="var(--navy-deep)"/>
    <polygon points="735,0 910,0 910,438 640,438" fill="var(--blue)"/>
    <polygon points="735,0 760,0 700,96 680,96" fill="var(--red-dark)"/>
  </svg>

  <h2 class="abs title-back">DOMESTIC VIOLENCE</h2>
  <p class="abs lede">Dwight decided to run because no one on the school board would terminate Dwight's ex and her new boyfriend who both work for the school district. His ex even filed criminal charges against him that are still pending.</p>

  <div class="abs stamp">STAMP</div>
  <div class="abs address">ADDRESS</div>

  <div class="abs mug mug-left"><span role="img" aria-label="Booking photo, profile facing left"></span></div>
  <div class="abs charges">CRIMINAL TRESPASS<br>&amp; CRIMINAL MISCHIEF</div>
  <div class="abs mug mug-center"><span role="img" aria-label="Booking photo, full face"></span></div>
  <div class="abs mug mug-right"><span role="img" aria-label="Booking photo, profile facing right"></span></div>

  <div class="abs complaint complaint-one">
    <div class="head"><span>THE STATE OF TEXAS<br>COUNTY OF MARLOW</span><span>CR-21-40217-K</span></div>
    <p>IN THE NAME AND BY AUTHORITY OF THE STATE OF TEXAS:<br>Before me, the undersigned assistant attorney, appeared the affiant, who under oath says he believes the following is true.</p>
    <p>DWIGHT KESSLER, on or about the 28th day of September, did knowingly damage tangible property, namely garage lights, without consent of the owner, Carla Ostrand.</p>
    <p>AGAINST THE PEACE AND DIGNITY OF THE STATE.</p>
    <div class="sign"><span>Filed for record</span><span>(Affiant)</span></div>
    <div class="sign"><span>Sworn to and subscribed before me on<span class="sign-line"></span></span><span>Assistant District Attorney, Marlow County</span></div>
  </div>

  <div class="abs complaint complaint-two">
    <div class="head"><span>THE STATE OF TEXAS<br>COUNTY OF MARLOW</span><span>CR-21-40217-K</span></div>
    <p>IN THE NAME AND BY AUTHORITY OF THE STATE OF TEXAS:<br>Before me, the undersigned assistant attorney, appeared the affiant, who under oath says he believes the following is true.</p>
    <p>DWIGHT KESSLER, on or about the 28th day of September, did knowingly damage tangible property, namely garage lights, without consent of the owner, Carla Ostrand.</p>
    <p>AGAINST THE PEACE AND DIGNITY OF THE STATE.</p>
    <div class="sign"><span>Filed for record</span><span>(Affiant)</span></div>
    <div class="sign"><span>Sworn to and subscribed before me on<span class="sign-line"></span></span><span>Assistant District Attorney, Marlow County</span></div>
  </div>

  <p class="abs goal">Dwight's ultimate goal is to terminate his ex and her new boyfriend if elected. Plus Gordon Pruett needs the majority on the school board to do what he does bet.</p>

  <div class="abs kickbacks">Kickbacks<br>for Contracts.</div>
  <div class="abs contractors">THEY WILL HIRE<br>THEIR OWN CONTRACTORS</div>

  <div class="abs footer"><span class="say">Say "No"</span><span class="rest">to Dwight's Revenge &amp; Gordon Pruett Money Grab!</span></div>
</section>

</body>
</html>
```